Pull Up Banners

Would like to have these pull up banner designs changed to a new modern theme. I have running a sales booth and want to re-design the banner designs. I have uploaded old banner design, I need phone number and website added onto bottom. Happy to consider images to attract people attention to increase sales and spark people interest walking past.

```html
<!DOCTYPE html>
<html lang="en">
<head>
<meta charset="UTF-8">
<title>NEXORA Pull Up Banners</title>
<link href="https://fonts.googleapis.com/css2?family=Michroma&family=Roboto+Condensed:wght@500&family=Montserrat:wght@500;600&family=Lato:ital@1&family=Roboto:wght@400&display=swap" rel="stylesheet">
<style>
  :root{
    --board:#939598;
    --banner:#000000;
    --orange:#f26b21;
    --gold:#f7b34c;
    --silver:#d2d3d5;
    --white:#ffffff;
    --blue-deep:#041226;
    --teal:#1fb3b0;
  }
  *{margin:0;padding:0;box-sizing:border-box}
  html,body{width:1200px;height:1000px;overflow:hidden}
  body{background:var(--board);position:relative;font-family:"Roboto",sans-serif}
  .size-label{position:absolute;top:66px;font-size:15px;color:var(--white);font-family:"Roboto",sans-serif}
  .board-note{position:absolute;top:936px;left:0;width:100%;text-align:center;font-size:15px;color:var(--white)}
  .banner{position:absolute;top:90px;width:328px;height:820px;background:var(--banner);overflow:hidden}
  .banner--cloud{left:243px}
  .banner--managed{left:627px}
  .brand{position:absolute;top:70px;left:0;width:100%;text-align:center;z-index:2}
  .brand-mark{display:inline-flex;align-items:center;gap:9px}
  .brand-dot{width:18px;height:18px;border-radius:50%;background:var(--orange)}
  .brand-name{font-family:"Montserrat",sans-serif;font-weight:600;font-size:30px;color:var(--white);letter-spacing:3px;line-height:1}
  .brand-tagline{margin-top:7px;font-family:"Roboto",sans-serif;font-size:7px;letter-spacing:1.4px;color:var(--white)}
  .hero{position:absolute;left:0;width:100%}
  .hero--cloud{top:130px;height:326px;background:radial-gradient(circle at 50% 38%,#8fd3ff 0%,#2a86e6 12%,#0d3f8c 38%,var(--blue-deep) 70%,#02060d 100%)}
  .hero--managed{top:129px;height:330px;background:radial-gradient(ellipse at 52% 60%,#7ff2ea 0%,var(--teal) 10%,#0e3a40 35%,#060a0c 70%),linear-gradient(90deg,#3a1405,#000 40%,#000 60%,#5a2a08)}
  .hero--managed::after{content:"";position:absolute;inset:0;background:linear-gradient(90deg,rgba(242,107,33,.35),transparent 35%,transparent 65%,rgba(247,179,76,.4))}
  .heading{position:absolute;left:0;width:100%;text-align:center;font-family:"Michroma",sans-serif;color:var(--silver);font-weight:700;line-height:1.15;z-index:2}
  .heading--cloud{top:432px;font-size:18.5px}
  .heading--managed{top:430px;font-size:19.5px}
  .services{position:absolute;list-style:none}
  .services--cloud{top:522px;left:44px}
  .services--managed{top:500px;left:42px}
  .service{display:flex;align-items:center;height:37.7px;font-family:"Roboto Condensed",sans-serif;font-weight:500;font-size:20px;color:var(--gold)}
  .service svg{width:16px;height:16px;margin-right:10px;flex:none}
  .cta{position:absolute;top:709px;left:0;width:100%;text-align:center}
  .cta-lead{font-family:"Lato",sans-serif;font-style:italic;font-size:10px;color:var(--orange)}
  .cta-phone{font-family:"Montserrat",sans-serif;font-weight:500;font-size:34px;color:var(--white);letter-spacing:1px;line-height:1.1}
  .web-band{position:absolute;bottom:0;left:0;width:100%;height:51px;background:var(--orange);text-align:center;padding-top:5px}
  .web-lead{font-family:"Lato",sans-serif;font-style:italic;font-size:10px;color:var(--white)}
  .web-url{font-family:"Montserrat",sans-serif;font-weight:500;font-size:17px;color:var(--white);line-height:1.1}
</style>
</head>
<body>
  <div class="size-label" style="left:454px">Size 80x200 cm</div>
  <div class="size-label" style="left:842px">Size 80x200 cm</div>

  <section class="banner banner--cloud">
    <div class="hero hero--cloud" role="img" aria-label="Photo of a hand touching a glowing network of technology icons on a deep blue background"></div>
    <header class="brand">
      <div class="brand-mark"><span class="brand-dot"></span><span class="brand-name">NEXORA</span></div>
      <div class="brand-tagline">SMART TECH SUPPORT FOR EVERY BUSINESS</div>
    </header>
    <h2 class="heading heading--cloud">CLOUD<br>PHONE SYSTEM<br>&amp; INTERNET</h2>
    <ul class="services services--cloud">
      <li class="service"><svg viewBox="0 0 16 16"><path d="M3 1l3 3-1.5 2c1 2 2.5 3.5 4.5 4.5L11 9l3 3-2 2C6 13 2 8 1 3z" fill="#fff"/></svg>VoIP &amp; Phone Systems</li>
      <li class="service"><svg viewBox="0 0 16 16"><path d="M1 2h14v10H5l-3 3v-3H1z" fill="#fff"/><path d="M4 5h8M4 8h8" stroke="#000" stroke-width="1.2"/></svg>SMS Gateway</li>
      <li class="service"><svg viewBox="0 0 16 16" fill="#fff"><circle cx="8" cy="5" r="2.5"/><circle cx="3" cy="6" r="1.8"/><circle cx="13" cy="6" r="1.8"/><path d="M3 13c0-3 2-4.5 5-4.5s5 1.5 5 4.5z"/><path d="M0 12c0-2 1-3 3-3h1c-1 1-1.5 2-1.5 3zM16 12c0-2-1-3-3-3h-1c1 1 1.5 2 1.5 3z"/></svg>Workhub Team Calling</li>
      <li class="service"><svg viewBox="0 0 16 16" fill="none" stroke="#fff" stroke-width="1.5" stroke-linecap="round"><path d="M1 6a10 10 0 0 1 14 0M3.5 8.5a6.5 6.5 0 0 1 9 0M6 11a3 3 0 0 1 4 0"/><circle cx="8" cy="13.5" r=".8" fill="#fff"/></svg>Broadband, Fibre &amp; 4G Internet</li>
    </ul>
    <div class="cta"><div class="cta-lead">Call to find out more</div><div class="cta-phone">000 000 000</div></div>
    <footer class="web-band"><div class="web-lead">Visit our website for more</div><div class="web-url">nexorait.com.au</div></footer>
  </section>

  <section class="banner banner--managed">
    <div class="hero hero--managed" role="img" aria-label="Digital artwork of a data tunnel with streaks of orange and teal light"></div>
    <header class="brand">
      <div class="brand-mark"><span class="brand-dot"></span><span class="brand-name">NEXORA</span></div>
      <div class="brand-tagline">SMART TECH SUPPORT FOR EVERY BUSINESS</div>
    </header>
    <h2 class="heading heading--managed">MANAGED<br>I.T SERVICES</h2>
    <ul class="services services--managed">
      <li class="service"><svg viewBox="0 0 16 16" fill="none" stroke="#fff" stroke-width="1.5"><rect x="1" y="2" width="14" height="9"/><path d="M8 11v3M4 14h8"/></svg>Managed I.T Support</li>
      <li class="service"><svg viewBox="0 0 16 16" fill="none" stroke="#fff" stroke-width="1.4"><path d="M8 1l6 2.5v4c0 4-3 6.5-6 7.5-3-1-6-3.5-6-7.5v-4z"/><rect x="5.5" y="7" width="5" height="4"/><path d="M6.5 7V5.5a1.5 1.5 0 0 1 3 0V7"/></svg>Cybersecurity Solutions</li>
      <li class="service"><svg viewBox="0 0 16 16" fill="none" stroke="#fff" stroke-width="1.4"><path d="M4 9a3 3 0 0 1 0-6 4 4 0 0 1 8 1 2.5 2.5 0 0 1 0 5z"/><path d="M5 9v4M8 9v5M11 9v4"/></svg>Cloud Servers &amp; Backups</li>
      <li class="service"><svg viewBox="0 0 16 16" fill="none" stroke="#fff" stroke-width="1.5"><rect x="1" y="3" width="14" height="10"/><path d="M1 3l7 6 7-6"/></svg>Workhub Email Packs</li>
      <li class="service"><svg viewBox="0 0 16 16" fill="none" stroke="#fff" stroke-width="1.2"><circle cx="8" cy="8" r="6.5"/><ellipse cx="8" cy="8" rx="3" ry="6.5"/><path d="M1.5 8h13M2.5 5h11M2.5 11h11"/></svg>Domains &amp; Websites</li>
    </ul>
    <div class="cta"><div class="cta-lead">Call to find out more</div><div class="cta-phone">000 000 000</div></div>
    <footer class="web-band"><div class="web-lead">Visit our website for more</div><div class="web-url">nexorait.com.au</div></footer>
  </section>

  <p class="board-note">Plz. provide your phone number for ad this</p>
</body>
</html>
```